Poster Required for Cafe to promote Catering

I would like a Poster made to advertise that our business does catering.
On the poster we would like it to say:

Did you know that Sunny Ladle does Catering?
We offer Breakfast, Lunch, Morning and Afternoon Tea Options
Come instore to enquire

At the bottom of the flyer, can you please put the contact details:
Phone 0487 602 914
Email tam@sunnyladlecanteen.com

Poster Size A3

I have attached our logo and menu's so you can get a feel for what we like.

Target Market(s)

Hospital Staff: Doctors, Nurses, Admin

Industry/Entity Type

Hospitality

Requirements
Nice to have
• Some pictures of catering. Eg. Gourmet Sandwiches, Sliders
• You could check our instagram page for ideas on what we do..
• @snyladle_qld

```html
<!DOCTYPE html>
<html lang="en">
<head>
<meta charset="utf-8">
<title>Sunny Ladle Catering Poster</title>
<link rel="stylesheet" href="https://fonts.googleapis.com/css2?family=Kalam:wght@400;700&display=swap">
<style>
  :root {
    --page: #ffffff;
    --board: #412f30;
    --chalk: #f8f39c;
    --chalk-soft: #5b4743;
  }
  * { margin: 0; padding: 0; box-sizing: border-box; }
  html, body {
    width: 1200px; height: 1000px; overflow: hidden;
    background: var(--page);
  }
  .canvas { position: relative; width: 1200px; height: 1000px; }
  .poster {
    position: absolute; left: 316px; top: 86px;
    width: 600px; height: 846px;
    background: var(--board);
    font-family: "Kalam", cursive;
    color: var(--chalk);
  }
  .poster > * { position: absolute; }
  .logo-mark {
    left: 222px; top: 24px; width: 134px; height: 115px;
    background: var(--chalk);
    display: flex; align-items: center; justify-content: center;
    text-align: center;
  }
  .logo-mark span {
    font-weight: 700; font-size: 17px; line-height: 1.05;
    color: var(--board); letter-spacing: 1px; text-transform: uppercase;
  }
  .decor { left: 0; top: 0; width: 600px; height: 846px; }
  .food-art { fill: var(--chalk-soft); }
  .headline {
    left: 230px; top: 178px; width: 180px;
    font-weight: 700; font-size: 34px; line-height: 46px;
    text-align: left;
  }
  .headline .line-2 { display: block; padding-left: 22px; }
  .brand-name {
    left: 160px; top: 455px; width: 290px; text-align: center;
    font-weight: 700; font-size: 38px; line-height: 38px;
    letter-spacing: 4px; text-transform: uppercase;
  }
  .question {
    left: 150px; top: 540px; width: 300px; text-align: center;
    font-weight: 700; font-size: 30px; line-height: 40px;
  }
  .question small { font-size: 21px; margin-right: 6px; }
  .offer {
    left: 60px; top: 610px; width: 470px; text-align: center;
    font-size: 21px; line-height: 26.5px; font-style: italic;
  }
  .contact {
    left: 40px; top: 740px; width: 520px; text-align: center;
    font-size: 23px; line-height: 33px; font-style: italic;
  }
  .contact a {
    color: var(--chalk); text-decoration: underline;
    text-underline-offset: 4px;
  }
</style>
</head>
<body>
<div class="canvas">
  <section class="poster">
    <svg class="decor" viewBox="0 0 600 846" aria-hidden="false">
      <g stroke="var(--chalk)" stroke-width="3" stroke-linecap="round" fill="none" class="logo-rays">
        <line x1="150" y1="44" x2="175" y2="50"/>
        <line x1="148" y1="78" x2="178" y2="70"/>
        <line x1="158" y1="112" x2="183" y2="98"/>
        <line x1="404" y1="44" x2="428" y2="28"/>
        <line x1="406" y1="62" x2="440" y2="60"/>
        <line x1="404" y1="98" x2="430" y2="108"/>
      </g>
      <ellipse class="food-art" role="img" aria-label="Chalk drawing of a takeaway coffee cup in a cloud" cx="134" cy="224" rx="78" ry="72"/>
      <ellipse class="food-art" role="img" aria-label="Chalk drawing of a fruit basket in a cloud" cx="488" cy="208" rx="76" ry="66"/>
      <ellipse class="food-art" role="img" aria-label="Chalk drawing of eggs frying in a pan in a cloud" cx="324" cy="360" rx="108" ry="68"/>
      <ellipse class="food-art" role="img" aria-label="Chalk drawing of a gourmet sandwich in a cloud" cx="120" cy="410" rx="94" ry="78"/>
      <ellipse class="food-art" role="img" aria-label="Chalk drawing of a muffin in a cloud" cx="492" cy="424" rx="76" ry="78"/>
      <g class="offer-frame" stroke="var(--chalk)" stroke-width="3" fill="none" stroke-linejoin="round">
        <path d="M64 604 L524 602 L522 710 L74 712 Z"/>
        <path d="M54 614 L64 604 M54 614 L58 722 L74 712 M58 722 L516 728 L522 710"/>
      </g>
    </svg>

    <div class="logo-mark"><span>Sunny<br>Ladle</span></div>

    <h1 class="headline">Did you<span class="line-2">know</span></h1>
    <p class="brand-name">Sunny<br>Ladle</p>
    <p class="question"><small>does</small>Catering?</p>

    <p class="offer">We offer Breakfast, Lunch and<br>Morning and Afternoon Tea Options<br>Come instore to enquire</p>

    <p class="contact">
      Phone <a href="tel:0487602914">0487-602-914</a><br>
      Email <a href="mailto:tam@sunnyladlecanteen.com">tam@sunnyladlecanteen.com</a>
    </p>
  </section>
</div>
</body>
</html>
```